New Property management company business cards

Looking for a new business card, to reflect new younger ownership
Card should be clean, simple and professional but with a modern layout that is conveys our new logo and business model

Key aspects of the business:

Property Management
Facility Maintenance
Project Management
Tenant Improvements

Mailing Address:
PO BOX 7816
Brookvale CA, 95368

Phone: 209-418-6071
Direct: 209-418-6074

Doyle Marsh
President

Target Market(s)

Commercial property owners

Industry/Entity Type

Real Estate property management

Contact Information for Business Card

Open to all designs but lean toward vertical layouts

Requirements
Must have
• Logo and space to customize name and contact info

```html
<!DOCTYPE html>
<html lang="en">
<head>
<meta charset="utf-8">
<title>Valmora Property Management – Business Card</title>
<link href="https://fonts.googleapis.com/css2?family=Poppins:wght@400;500;600&display=swap" rel="stylesheet">
<style>
  :root {
    --bg: #e1e1e1;
    --navy: #32313f;
    --teal: #1fb0a6;
    --white: #ffffff;
    --rule: #8a8996;
  }
  * { margin: 0; padding: 0; box-sizing: border-box; }
  html, body { width: 791px; height: 1200px; overflow: hidden; }
  body { background: var(--bg); font-family: "Poppins", sans-serif; position: relative; }

  .card { position: absolute; box-shadow: 0 8px 14px rgba(0,0,0,.22); overflow: hidden; }

  /* Front */
  .card-front { left: 108px; top: 122px; width: 576px; height: 329px; background: var(--navy); color: var(--white); }
  .brand-front { position: absolute; top: 96px; left: 0; width: 100%; text-align: center;
    font-size: 32px; font-weight: 500; letter-spacing: 9px; line-height: 1; }
  .brand-mark { display: inline-block; width: 12px; height: 12px; background: var(--teal); margin-right: 10px; vertical-align: middle; position: relative; top: -3px; }
  .service { position: absolute; top: 166px; width: 120px; margin-left: -60px; text-align: center; }
  .service svg { display: block; margin: 0 auto; }
  .service-name { margin-top: 7px; font-size: 13.5px; font-weight: 600; line-height: 16.5px; }
  .website { position: absolute; top: 277px; left: 0; width: 100%; text-align: center;
    font-size: 13px; font-weight: 600; letter-spacing: 5px; }

  /* Back */
  .card-back { left: 231px; top: 503px; width: 329px; height: 576px; background: var(--navy); color: var(--white); }
  .back-top { position: absolute; left: 0; top: 0; width: 100%; height: 241px; background: var(--white); }
  .brand-back { position: absolute; top: 144px; left: 0; width: 100%; text-align: center;
    color: var(--navy); font-size: 38px; font-weight: 500; letter-spacing: 8px; line-height: 1; }
  .brand-back .brand-mark { width: 14px; height: 14px; margin-right: 8px; top: -5px; }
  .tagline { position: absolute; top: 184px; left: 0; width: 100%; text-align: center;
    color: var(--navy); font-size: 12px; letter-spacing: 6.2px; padding-left: 6px; }
  .tab { position: absolute; left: 89px; top: 241px; }
  .person { position: absolute; left: 64px; top: 275px; }
  .person-name { font-size: 23px; font-weight: 600; line-height: 1; }
  .person-name .surname { color: var(--teal); }
  .person-title { margin-top: 8px; font-size: 13px; letter-spacing: 9.3px; }
  .divider { position: absolute; left: 66px; right: 0; top: 338px; height: 1px; background: var(--rule); }
  .contact { position: absolute; left: 66px; }
  .contact-icon { position: absolute; left: 0; top: 6px; width: 16px; height: 20px; }
  .contact-text { position: absolute; left: 37px; top: 0; white-space: nowrap; }
  .contact-label { color: var(--teal); font-size: 15px; font-weight: 500; line-height: 16.5px; }
  .contact-value { font-size: 15px; font-weight: 500; line-height: 17px; letter-spacing: .3px; }
</style>
</head>
<body>

<section class="card card-front" aria-label="Card front">
  <div class="brand-front"><span class="brand-mark"></span>VALMORA</div>

  <div class="service" style="left:104px">
    <svg width="66" height="64" viewBox="0 0 66 64" role="img" aria-label="Property management icon">
      <polygon points="2,30 33,61 64,30 58,30 33,55 8,30" fill="var(--teal)"/>
      <polygon points="33,0 62,29 33,58 4,29" fill="var(--white)"/>
    </svg>
    <div class="service-name">Property<br>Management</div>
  </div>
  <div class="service" style="left:226px">
    <svg width="66" height="64" viewBox="0 0 66 64" role="img" aria-label="Facility maintenance icon">
      <polygon points="2,30 33,61 64,30 58,30 33,55 8,30" fill="var(--teal)"/>
      <polygon points="33,0 62,29 33,58 4,29" fill="var(--white)"/>
    </svg>
    <div class="service-name">Facility<br>Maintenance</div>
  </div>
  <div class="service" style="left:350px">
    <svg width="66" height="64" viewBox="0 0 66 64" role="img" aria-label="Project management icon">
      <polygon points="2,30 33,61 64,30 58,30 33,55 8,30" fill="var(--teal)"/>
      <polygon points="33,0 62,29 33,58 4,29" fill="var(--white)"/>
    </svg>
    <div class="service-name">Project<br>Management</div>
  </div>
  <div class="service" style="left:474px">
    <svg width="66" height="64" viewBox="0 0 66 64" role="img" aria-label="Tenant improvements icon">
      <polygon points="2,30 33,61 64,30 58,30 33,55 8,30" fill="var(--teal)"/>
      <polygon points="33,0 62,29 33,58 4,29" fill="var(--white)"/>
    </svg>
    <div class="service-name">Tenant<br>Improvements</div>
  </div>

  <div class="website">www.valmorapm.com</div>
</section>

<section class="card card-back" aria-label="Card back">
  <div class="back-top">
    <div class="brand-back"><span class="brand-mark"></span>VALMORA</div>
    <div class="tagline">PROPERTY MANAGEMENT</div>
  </div>
  <svg class="tab" width="152" height="12" viewBox="0 0 152 12" aria-hidden="true">
    <polygon points="0,0 152,0 144,12 8,12" fill="var(--white)"/>
    <polygon points="4,0 148,0 142,9 10,9" fill="var(--teal)"/>
  </svg>

  <div class="person">
    <div class="person-name">Doyle <span class="surname">Marsh</span></div>
    <div class="person-title">PRESIDENT</div>
  </div>
  <div class="divider"></div>

  <div class="contact" style="top:360px">
    <svg class="contact-icon" viewBox="0 0 16 20" aria-hidden="true">
      <rect x="3" y="1" width="10" height="18" rx="1.5" fill="none" stroke="var(--teal)" stroke-width="1.6"/>
      <circle cx="8" cy="16" r="1" fill="var(--teal)"/>
    </svg>
    <div class="contact-text">
      <div class="contact-label">Phone:</div>
      <div class="contact-value">209-418-6071</div>
    </div>
  </div>

  <div class="contact" style="top:407px">
    <svg class="contact-icon" viewBox="0 0 16 20" aria-hidden="true">
      <path d="M1 9 Q8 3 15 9 L13 11 L11 9 L5 9 L3 11 Z" fill="var(--teal)"/>
      <rect x="3" y="10" width="10" height="6" rx="1" fill="var(--teal)"/>
    </svg>
    <div class="contact-text">
      <div class="contact-label">Direct:</div>
      <div class="contact-value">209-418-6074</div>
    </div>
  </div>

  <div class="contact" style="top:454px">
    <svg class="contact-icon" viewBox="0 0 16 20" aria-hidden="true">
      <path d="M1 8 L8 3 L15 8 L15 17 L1 17 Z" fill="none" stroke="var(--teal)" stroke-width="1.5"/>
      <path d="M1 8 L8 13 L15 8" fill="none" stroke="var(--teal)" stroke-width="1.5"/>
      <circle cx="8" cy="8" r="2" fill="none" stroke="var(--teal)" stroke-width="1.2"/>
    </svg>
    <div class="contact-text">
      <div class="contact-label">Email:</div>
      <div class="contact-value">Doyle@valmorapm.com</div>
    </div>
  </div>

  <div class="contact" style="top:501px">
    <svg class="contact-icon" viewBox="0 0 16 20" aria-hidden="true">
      <rect x="1" y="5" width="14" height="10" fill="var(--teal)"/>
      <path d="M1 5 L8 11 L15 5 M1 15 L6 9 M15 15 L10 9" fill="none" stroke="var(--navy)" stroke-width="1.1"/>
    </svg>
    <div class="contact-text">
      <div class="contact-label">Mailing Address:</div>
      <div class="contact-value">PO BOX 7816<br>Brookvale CA, 95368</div>
    </div>
  </div>
</section>

</body>
</html>
```